We need visit card and a letter paper for our website. thx

We have a beauty clinic in Switzerland.
https://wolkenbachtal.ch
We need a visit card.

Requirements
Must have
• see colors on website

```html
<!DOCTYPE html>
<html lang="en">
<head>
<meta charset="utf-8">
<title>Wolkenbachtal – Business Card</title>
<link rel="stylesheet" href="https://fonts.googleapis.com/css2?family=Jost:wght@300;400&family=Arimo:wght@400;700&display=swap">
<style>
  :root {
    --backdrop: #2a2a2a;
    --card: #1f1f1f;
    --band: #5c5c5c;
    --white: #ffffff;
    --soft: #d8d8d8;
    --photo-a: #6e6e6e;
    --photo-b: #9a9a9a;
  }
  * { box-sizing: border-box; margin: 0; padding: 0; }
  html, body { width: 1200px; height: 900px; overflow: hidden; }
  body {
    background: var(--backdrop);
    font-family: "Arimo", Arial, sans-serif;
    color: var(--white);
    position: relative;
  }
  .card {
    position: absolute;
    left: 320px;
    width: 560px;
    height: 340px;
    background: var(--card);
    border-radius: 3px;
    overflow: hidden;
  }
  .card-front { top: 80px; }
  .card-back { top: 480px; }

  /* Front */
  .brand {
    position: absolute;
    left: 0; right: 0; top: 118px;
    text-align: center;
  }
  .brand-name {
    font-family: "Jost", sans-serif;
    font-weight: 400;
    font-size: 46px;
    letter-spacing: 0.5px;
    color: var(--white);
  }
  .brand-web {
    margin-top: 22px;
    font-family: "Jost", sans-serif;
    font-weight: 300;
    font-size: 13px;
    letter-spacing: 3px;
    color: var(--soft);
  }

  /* Back */
  .hotline-band {
    position: absolute;
    left: 0; right: 0;
    top: 222px; height: 78px;
    background: var(--band);
  }
  .team { position: absolute; inset: 0; }
  .doctor { position: absolute; width: 130px; }
  .doctor-a { left: 34px; top: 26px; }
  .doctor-b { left: 170px; top: 64px; }
  .portrait {
    width: 112px; height: 100px;
    background: linear-gradient(160deg, var(--photo-b), var(--photo-a));
  }
  .doctor-name {
    margin-top: 14px;
    padding-left: 10px;
    font-size: 16px;
    font-weight: 700;
    line-height: 1.15;
  }
  .doctor-name .title { font-weight: 400; }
  .contact {
    position: absolute;
    left: 312px; top: 112px;
    font-size: 15px;
    line-height: 1.3;
    color: var(--soft);
  }
  .contact-line { display: flex; align-items: center; gap: 7px; }
  .address { margin-bottom: 8px; }
  .contact svg { width: 15px; height: 15px; flex: none; }
  .hotline {
    position: absolute;
    left: 32px; top: 262px;
    font-size: 16px;
    color: var(--soft);
  }
  .hotline strong {
    font-size: 21px;
    color: var(--white);
    margin-left: 4px;
  }
</style>
</head>
<body>

<section class="card card-front">
  <div class="brand">
    <div class="brand-name">Wolkenbachtal</div>
    <div class="brand-web">www.wolkenbachtal.ch</div>
  </div>
</section>

<section class="card card-back">
  <div class="hotline-band"></div>

  <div class="team">
    <div class="doctor doctor-a">
      <div class="portrait" role="img" aria-label="Black and white portrait of Dr. Lena Marbach"></div>
      <div class="doctor-name">Dr. Lena<br>Marbach</div>
    </div>
    <div class="doctor doctor-b">
      <div class="portrait" role="img" aria-label="Black and white portrait of Dr. Felix Oberhauser"></div>
      <div class="doctor-name">Dr. Felix<br>Oberhauser<span class="title">, DESA</span></div>
    </div>
  </div>

  <div class="contact">
    <div class="address">Talweg 14<br>7412 Wolkenbach, Switzerland</div>
    <div class="contact-line">
      <svg viewBox="0 0 16 16" aria-hidden="true"><rect x="1" y="3" width="14" height="10" fill="none" stroke="#fff" stroke-width="1.4"/><path d="M1 3l7 6 7-6" fill="none" stroke="#fff" stroke-width="1.4"/></svg>
      <span>hallo@wolkenbachtal.ch</span>
    </div>
    <div class="contact-line">
      <svg viewBox="0 0 16 16" aria-hidden="true"><circle cx="8" cy="8" r="6.5" fill="none" stroke="#fff" stroke-width="1.3"/><ellipse cx="8" cy="8" rx="3" ry="6.5" fill="none" stroke="#fff" stroke-width="1.1"/><path d="M1.5 8h13M2.5 5h11M2.5 11h11" stroke="#fff" stroke-width="1"/></svg>
      <span>www.wolkenbachtal.ch</span>
    </div>
  </div>

  <div class="hotline">Free 24-hour beauty hotline: <strong>+41 (0) 800 24 60 60</strong></div>
</section>

</body>
</html>
```